MD Trailcraft & Wildland Expo

I need a 1 page flyer for promotion of an upcoming sportsman and outdoor show(expo). would like the flyer to be able to be printed in B&W and color! show will include all things to do with the out doors, hunting fishing boating hiking atv camping rvs motorcycles. the event will have a kids zone, events games and activities for kids. there will be vendors showing the newest products. guest speakers and industry experts giving training and advice. this show will have something for everyone. food trucks and concessions. 200+ vendors. waterfould calling competition. deer/buck scoring casting competition for kids 3D Archery competitions

Target Market(s)

anyone event open to all ages!

Colors
ec1f27
000000
fbed22

Requirements
Must have
• date- september 1-2 2018
• location Penwick county fair 4817 millbrook rd east caldon MD 21638
• facebook - mdtrailcraftexpo
• email mdtrailcraftexpo@mailvento.com
• web www.mdtrailcraftexpo-demo.com
• vendor spaces still available! sign up now space going fast
Nice to have
• would like some thing that can be both printed in B&W and Color, and still have a great affect.
Should not have
• open to any suggestions

```html
<!DOCTYPE html>
<html lang="en">
<head>
<meta charset="utf-8">
<title>MD Trailcraft &amp; Wildland Expo</title>
<link rel="stylesheet" href="https://fonts.googleapis.com/css2?family=Oswald:wght@700&family=Lato:wght@400;700;900&display=swap">
<style>
  :root {
    --red: #ec1f27;
    --black: #000000;
    --yellow: #fbed22;
    --orange: #f4772a;
    --ink: #1d1d1d;
    --body: #3a3a3a;
    --backdrop: #8a8a8a;
    --white: #ffffff;
  }
  * { box-sizing: border-box; margin: 0; padding: 0; }
  html, body { width: 1128px; height: 1200px; overflow: hidden; background: var(--backdrop); }
  .flyer {
    position: absolute; left: 100px; top: 0;
    width: 1151px; height: 1490px;
    transform: scale(0.8054); transform-origin: 0 0;
    background: var(--white); overflow: hidden;
    font-family: "Lato", sans-serif; color: var(--body);
  }
  .hero { position: absolute; left: 0; top: 0; width: 1151px; height: 620px; }
  .title {
    position: absolute; left: 0; width: 1151px; text-align: center;
    font-family: "Oswald", sans-serif; font-weight: 700; color: var(--white);
    letter-spacing: 3px; -webkit-text-stroke: 2px var(--black);
    text-shadow: 3px 3px 0 var(--black); transform: translateX(-5px);
  }
  .title--main { top: 188px; font-size: 66px; line-height: 1; }
  .title--sub { top: 268px; font-size: 56px; line-height: 1; }
  .title--date { top: 344px; font-size: 42px; line-height: 1; letter-spacing: 1px; }
  .title--date .month { color: var(--red); }
  .photo-circle {
    position: absolute; width: 290px; height: 290px; border-radius: 50%;
    border: 10px solid var(--black);
  }
  .photo-circle--hike { left: 832px; top: 338px; background: radial-gradient(circle at 50% 30%, #dfe9f0, #b7a47c 55%, #6c5a36); }
  .photo-circle--camp { left: 832px; top: 642px; border-color: var(--red); background: linear-gradient(#e7a45a, #c46a2e 45%, #5e3b20 80%, #2f2414); }
  .photo-circle--field { left: 832px; top: 946px; background: linear-gradient(#9fb3c2, #d3a861 50%, #a2782f 80%, #5b4218); }
  .vendors {
    position: absolute; left: 35px; top: 620px;
    font-family: "Oswald", sans-serif; font-weight: 700; font-size: 44px;
    color: var(--red); letter-spacing: 4px; line-height: 1.1;
  }
  .social { position: absolute; left: 38px; top: 670px; font-size: 26px; font-weight: 700; color: var(--ink); }
  .features { position: absolute; left: 38px; top: 734px; font-size: 21.5px; line-height: 27px; }
  .features .free { color: var(--red); }
  .rule { position: absolute; left: 35px; width: 636px; height: 2px; background: var(--red); }
  .rule--top { top: 898px; }
  .rule--bottom { top: 1170px; }
  .space { position: absolute; left: 34px; top: 903px; font-size: 26px; line-height: 32px; font-weight: 700; color: var(--red); }
  .products { position: absolute; left: 38px; top: 985px; font-size: 21.5px; line-height: 27px; width: 700px; }
  .pitch { position: absolute; left: 131px; top: 1212px; font-size: 24px; line-height: 32px; font-weight: 900; color: var(--ink); }
  .pitch .expect { display: block; margin-top: 3px; color: var(--red); font-weight: 700; }
  .contact {
    position: absolute; left: 0; top: 1338px; width: 1151px; height: 152px;
    background: linear-gradient(90deg, var(--yellow), var(--orange) 50%, var(--red));
    color: var(--white);
  }
  .contact__title { position: absolute; left: 0; width: 1151px; top: 4px; text-align: center; font-size: 33px; font-weight: 900; letter-spacing: -0.5px; }
  .contact__list { position: absolute; list-style: none; font-weight: 700; }
  .contact__list li { position: relative; padding-left: 30px; }
  .contact__list li::before { content: ""; position: absolute; left: 0; top: 0.55em; width: 13px; height: 13px; border-radius: 50%; background: var(--white); }
  .contact__list--web { left: 114px; top: 58px; font-size: 27px; line-height: 37px; }
  .contact__list--venue { left: 610px; top: 64px; font-size: 21.5px; line-height: 27px; }
</style>
</head>
<body>
<main class="flyer">
  <svg class="hero" viewBox="0 0 1151 620" aria-hidden="false">
    <defs>
      <linearGradient id="lake" x1="0" y1="0" x2="0" y2="1">
        <stop offset="0" stop-color="#e4c46a"/>
        <stop offset="0.28" stop-color="#b9862e"/>
        <stop offset="0.38" stop-color="#d9a9a0"/>
        <stop offset="0.7" stop-color="#b97a86"/>
        <stop offset="1" stop-color="#8c6a5a"/>
      </linearGradient>
      <linearGradient id="angler" x1="0" y1="0" x2="1" y2="0">
        <stop offset="0" stop-color="#000" stop-opacity="0"/>
        <stop offset="1" stop-color="#3c3f26" stop-opacity="0.85"/>
      </linearGradient>
    </defs>
    <g role="img" aria-label="Photo of an angler holding a fishing rod and reel beside a sunlit lake">
      <rect width="1151" height="620" fill="url(#lake)"/>
      <rect x="700" width="451" height="620" fill="url(#angler)"/>
    </g>
    <path d="M0,300 C320,420 720,480 1151,470 L1151,505 C720,520 300,470 0,392 Z" fill="var(--black)"/>
    <path d="M0,398 C300,474 720,520 1151,510 L1151,520 C720,532 300,486 0,408 Z" fill="#6b5a8a" opacity="0.7"/>
    <path d="M0,412 C280,490 620,526 1151,516 L1151,540 C820,568 420,586 0,500 Z" fill="var(--red)"/>
    <path d="M0,500 C420,590 820,572 1151,540 L1151,620 L0,620 Z" fill="var(--white)"/>
  </svg>

  <h1 class="title title--main">MD TRAILCRAFT</h1>
  <div class="title title--sub">&amp; WILDLAND EXPO</div>
  <div class="title title--date"><span class="month">September</span> 1-2, 2018</div>

  <div class="photo-circle photo-circle--hike" role="img" aria-label="Photo of hikers walking a grassy trail"></div>
  <div class="photo-circle photo-circle--camp" role="img" aria-label="Photo of a red tent at a campsite at sunset"></div>
  <div class="photo-circle photo-circle--field" role="img" aria-label="Photo of a hunter aiming a rifle in tall grass"></div>

  <h2 class="vendors">Vendors Spaces Still Available</h2>
  <p class="social">Find Us on Friendbook.Com/Mdtrailcraftexpo</p>

  <p class="features">
    Deer &amp; Bear Scoring with Bucks-Bears-Stags (Bring Your Racks &amp; Skulls)<br>
    Waterfowl Calling Contest &#9679; Casting Competitions (Kids Zone)<br>
    <span class="free">FREE</span> Seminars, Displays, Hunting &amp; Fishing Outfitters,<br>
    Archery &amp; Guns, Fresh &amp; Saltwater Vendors, Boats, ATVs &amp; UTVs<br>
    Food &amp; Music
  </p>

  <div class="rule rule--top"></div>
  <p class="space">Over 60,000 sqft of INDOOR and 30,000+ sqft OUTDOOR<br>products and services including:</p>
  <p class="products">
    *Sports Equipment *Campers *Boats *RV’s<br>
    *Tackle &amp; Bait *Motorcycles *ATV’s *Trucks<br>
    *Taxidermists *Outfitters *Guns *Jet Skis *Charter Boats *Golf<br>
    Resorts *Knives *Archery *Trailers *Sporting Clubs *Game Calls *<br>
    Outdoor Magazines *Camp Grounds *Camping Equipment * Hunting<br>
    Supplies * and much more...
  </p>
  <div class="rule rule--bottom"></div>

  <p class="pitch">SELL YOUR PRODUCTS and SERVICES TO THOUSANDS OF PEOPLE<br>IN ONE WEEKEND!!
    <span class="expect">WE ARE EXPECTING 2 DAY ATTENDANCE TO TOP 15,000 PEOPLE!</span>
  </p>

  <footer class="contact">
    <h3 class="contact__title">CONTACT US TODAY</h3>
    <ul class="contact__list contact__list--web">
      <li>www.mdtrailcraftexpo-demo.com</li>
      <li>mdtrailcraftexpo@mailvento.com</li>
    </ul>
    <ul class="contact__list contact__list--venue">
      <li>Penwick county fair 4817 millbrook<br>rd east caldon MD 21638</li>
      <li>DANA 410-555-0188</li>
    </ul>
  </footer>
</main>
</body>
</html>
```